Business Card design for Founder and CEO of new shoe company

I am looking for a business card design for my new shoe company called Strido.

I am launching the company this April. Strido shoes offers slip-on athletic and casual style shoes for men and women. The unique selling point of the brand is that all of our shoe exist without shoelaces. I have included a link to the website to offer additional information about the company, see product images, and gain inspiration for the design. You can use the store owner password "Strido" to access the website.

www.Strido-shop.example

Thanks,
Dean Porlow

Target Market(s)

Active Men and Women ages 16-45

Industry/Entity Type

Business

Contact Information for Business Card

Dean Porlow
Founder and CEO
www.Strido-shop.example
deanporlow@Strido-shop.example
888-730-1964 / 888-7STRIDO
Strido, LLC
2384 N Tarrow St
Chicago, IL 60614

Requirements
Must have
• Be able to quickly and easily tell that Strido is a shoe company from the business card

```html
<!DOCTYPE html>
<html lang="en">
<head>
<meta charset="utf-8">
<title>Strido — Business Card</title>
<link rel="stylesheet" href="https://fonts.googleapis.com/css2?family=Open+Sans:wght@400;700&display=swap">
<style>
  :root {
    --backdrop: #6aa8c6;
    --sole-blue: #4fb8f6;
    --sole-dark: #363233;
    --pattern-light: #e9e9e9;
    --pattern-mid: #cfcfcf;
    --ink: #111111;
    --white: #ffffff;
    --shoe-blue: #2f8fd8;
    --shoe-dark: #1c2430;
  }
  html, body {
    margin: 0;
    padding: 0;
    width: 1200px;
    height: 1000px;
    overflow: hidden;
    background: var(--backdrop);
  }
  .canvas {
    position: relative;
    width: 1200px;
    height: 1000px;
    overflow: hidden;
    background: var(--backdrop);
    font-family: "Open Sans", Arial, sans-serif;
    color: var(--ink);
  }
  .soles {
    position: absolute;
    inset: 0;
  }
  .card-front, .card-back, .card-square {
    position: absolute;
    inset: 0;
    pointer-events: none;
  }
  .brand-name {
    position: absolute;
    font-family: "Open Sans", Arial, sans-serif;
    font-weight: 400;
    letter-spacing: 1px;
    line-height: 1;
    margin: 0;
  }
  .front-brand {
    left: 196px;
    top: 285px;
    font-size: 42px;
    color: var(--ink);
    display: flex;
    align-items: center;
    gap: 12px;
  }
  .brand-dot {
    width: 30px;
    height: 30px;
    border-radius: 50%;
    background: var(--ink);
    display: inline-block;
  }
  .product-photo {
    position: absolute;
    border-radius: 4px;
  }
  .front-photo {
    left: 216px;
    top: 345px;
    width: 176px;
    height: 96px;
    background: linear-gradient(180deg, var(--shoe-dark) 0%, var(--shoe-blue) 45%, var(--shoe-blue) 80%, #f2f6fa 100%);
  }
  .person-name {
    position: absolute;
    left: 198px;
    top: 555px;
    margin: 0;
    font-size: 21px;
    font-weight: 700;
    letter-spacing: 0.6px;
  }
  .person-title {
    position: absolute;
    left: 198px;
    top: 582px;
    margin: 0;
    font-size: 16px;
    font-weight: 400;
  }
  .contact-list {
    position: absolute;
    left: 198px;
    top: 624px;
    margin: 0;
    padding: 0;
    list-style: none;
    font-size: 14px;
    line-height: 18px;
  }
  .contact-list li {
    display: flex;
    align-items: center;
    gap: 6px;
  }
  .contact-icon {
    width: 12px;
    height: 12px;
    flex: none;
  }
  .address {
    position: absolute;
    left: 198px;
    top: 782px;
    margin: 0;
    font-style: normal;
    font-size: 14px;
    line-height: 18px;
  }
  .address-line { display: block; padding-left: 13px; }
  .address-line.first { padding-left: 0; display: flex; align-items: center; gap: 1px; }
  .square-card {
    position: absolute;
    left: 483px;
    top: 707px;
    width: 195px;
    height: 188px;
    background: var(--white);
  }
  .square-brand {
    left: 16px;
    top: 15px;
    font-size: 27px;
    color: var(--ink);
    display: flex;
    align-items: center;
    gap: 8px;
  }
  .square-brand .brand-dot { width: 20px; height: 20px; }
  .square-photo {
    left: 4px;
    top: 52px;
    width: 187px;
    height: 136px;
    border-radius: 0;
    background: linear-gradient(180deg, #f3f3f3 0%, var(--shoe-dark) 30%, var(--shoe-blue) 55%, var(--shoe-blue) 80%, #1b1b1b 100%);
  }
  .back-brand {
    left: 0;
    width: 1200px;
    padding-left: 0;
    top: 580px;
    display: flex;
    flex-direction: column;
    align-items: center;
    gap: 10px;
    color: var(--white);
    pointer-events: none;
  }
  .back-brand-wrap {
    position: absolute;
    left: 740px;
    top: 585px;
    width: 250px;
    display: flex;
    flex-direction: column;
    align-items: center;
    gap: 12px;
  }
  .back-brand-wrap .brand-dot {
    background: var(--white);
    width: 26px;
    height: 26px;
  }
  .back-brand-wrap .brand-name {
    position: static;
    font-size: 40px;
    color: var(--white);
  }
</style>
</head>
<body>
<main class="canvas">

  <svg class="soles" width="1200" height="1000" viewBox="0 0 1200 1000" aria-hidden="false">
    <defs>
      <clipPath id="back-sole-clip">
        <path d="M 800 132 C 880 132, 990 250, 1000 400 L 1008 860 C 1008 930, 950 962, 870 962 C 790 962, 735 930, 735 860 C 735 760, 720 640, 700 560 C 680 480, 665 420, 665 300 C 665 200, 720 132, 800 132 Z"/>
      </clipPath>
      <linearGradient id="pattern-tone" x1="0" y1="0" x2="1" y2="1">
        <stop offset="0" stop-color="var(--pattern-light)"/>
        <stop offset="1" stop-color="var(--pattern-mid)"/>
      </linearGradient>
    </defs>

    <!-- front of card: sole shape -->
    <path class="sole sole-front"
          fill="var(--sole-blue)"
          d="M 300 132 C 400 132, 470 200, 470 300 C 470 400, 402 450, 400 560 C 398 650, 425 700, 422 800 C 420 890, 370 930, 290 930 C 200 930, 165 880, 165 800 L 165 420 C 165 250, 200 132, 300 132 Z"/>

    <!-- back of card: sole shape -->
    <path class="sole sole-back"
          fill="var(--sole-dark)"
          d="M 800 132 C 880 132, 990 250, 1000 400 L 1008 860 C 1008 930, 950 962, 870 962 C 790 962, 735 930, 735 860 C 735 760, 720 640, 700 560 C 680 480, 665 420, 665 300 C 665 200, 720 132, 800 132 Z"/>

    <g clip-path="url(#back-sole-clip)">
      <path class="tread-area tread-forefoot" role="img"
            aria-label="Decorative tread pattern of interlocking white circles across the forefoot"
            fill="url(#pattern-tone)"
            d="M 790 140 C 870 140, 978 250, 990 400 C 990 470, 960 520, 925 560 L 790 560 C 760 520, 740 480, 720 440 C 695 390, 685 340, 690 290 C 700 200, 740 140, 790 140 Z"/>
      <path class="tread-area tread-heel" role="img"
            aria-label="Decorative tread pattern of interlocking white circles on the heel"
            fill="url(#pattern-tone)"
            d="M 870 690 C 900 720, 940 740, 944 800 C 946 880, 920 940, 870 944 C 815 944, 775 900, 770 820 C 768 760, 830 730, 870 690 Z"/>
    </g>
  </svg>

  <section class="card-front">
    <p class="brand-name front-brand"><span class="brand-dot"></span>Strido</p>
    <div class="product-photo front-photo" role="img" aria-label="Photo of a blue and black laceless athletic shoe"></div>

    <h1 class="person-name">DEAN PORLOW</h1>
    <p class="person-title">Founder and CEO</p>

    <ul class="contact-list">
      <li>
        <svg class="contact-icon" viewBox="0 0 12 12"><circle cx="6" cy="6" r="5" fill="none" stroke="#111" stroke-width="1"/><ellipse cx="6" cy="6" rx="2.2" ry="5" fill="none" stroke="#111" stroke-width="0.9"/><line x1="1" y1="6" x2="11" y2="6" stroke="#111" stroke-width="0.9"/></svg>
        www.Strido-shop.example
      </li>
      <li>
        <svg class="contact-icon" viewBox="0 0 12 12"><rect x="1" y="3" width="10" height="7" fill="#111"/><path d="M1 3 L6 7 L11 3" fill="none" stroke="#4fb8f6" stroke-width="0.9"/></svg>
        deanporlow@Strido-shop.example
      </li>
      <li>
        <svg class="contact-icon" viewBox="0 0 12 12"><rect x="1" y="1" width="10" height="10" rx="1.5" fill="#111"/><path d="M4 3.2 C3.4 5.5 5.5 8.3 8.6 8.6 L8.8 7.3 L7.4 6.8 L6.8 7.4 C5.8 6.9 5 6 4.7 5 L5.3 4.4 L4.9 3 Z" fill="#4fb8f6"/></svg>
        888-730-1964
      </li>
      <li>
        <svg class="contact-icon" viewBox="0 0 12 12"><path d="M1 5 C1 2.5 11 2.5 11 5 L9 5.6 L8.5 4.6 C7 4 5 4 3.5 4.6 L3 5.6 Z" fill="#111"/><rect x="3" y="6" width="6" height="4" rx="0.8" fill="#111"/></svg>
        888-7STRIDO
      </li>
    </ul>

    <address class="address">
      <span class="address-line first">
        <svg class="contact-icon" viewBox="0 0 12 12"><path d="M6 0.5 C3.6 0.5 2.2 2.3 2.2 4.2 C2.2 7 6 11.5 6 11.5 C6 11.5 9.8 7 9.8 4.2 C9.8 2.3 8.4 0.5 6 0.5 Z" fill="#111"/><circle cx="6" cy="4.2" r="1.4" fill="#4fb8f6"/></svg>
        Strido, LLC
      </span>
      <span class="address-line">2384 N Tarrow St</span>
      <span class="address-line">Chicago, IL 60614</span>
    </address>
  </section>

  <section class="card-square">
    <div class="square-card">
      <p class="brand-name square-brand"><span class="brand-dot"></span>Strido</p>
      <div class="product-photo square-photo" role="img" aria-label="Photo of a blue and black laceless athletic shoe on a dark surface"></div>
    </div>
  </section>

  <section class="card-back">
    <div class="back-brand-wrap">
      <span class="brand-dot"></span>
      <p class="brand-name">Strido</p>
    </div>
  </section>

</main>
</body>
</html>
```